Web Design for Rubbish Removal Company

I am looking for a custom web design that is clean and modern which also has a professional trustworthy feel to it.
The website is http://www.tidlowhaulage.com.au/ and need:
1 x Front Page
1 x Location Page
Please keep the green colour scheme as this is the corporate colours but would like to steer away from the black.
Industry/Entity Type
It Company
Number of Pages Required
2 page
Font styles to use
Sans Serif
Requirements
Must have
- Clean & Professional
- Keep green colour scheme
Should not have
- Steer away from black
- not look like a template

```html
<!DOCTYPE html>
<html lang="en">
<head>
<meta charset="utf-8">
<title>Tidlow Haulage – Sydney Rubbish Removal</title>
<link href="https://fonts.googleapis.com/css2?family=Montserrat:wght@300;400;500;600;700&family=Oswald:wght@400;500&display=swap" rel="stylesheet">
<style>
:root{
  --green:#76bd43;
  --green-dark:#5fa22f;
  --ink:#231f20;
  --text:#555;
  --muted:#888;
  --line:#e2e2e2;
  --white:#fff;
  --head:"Montserrat",sans-serif;
  --cond:"Oswald",sans-serif;
}
*{box-sizing:border-box;margin:0;padding:0}
html,body{width:1200px;height:3495px;overflow:hidden}
body{position:relative;font-family:var(--head);color:var(--text);background:var(--white)}
.abs{position:absolute}
a{color:inherit;text-decoration:none}

/* header */
.topbar{left:0;top:0;width:1200px;height:79px;background:var(--white)}
.brand{left:156px;top:22px;font:700 30px/36px var(--head);color:var(--ink);letter-spacing:-.5px}
.topbar-green{left:610px;top:0;width:590px;height:79px;background:var(--green);clip-path:polygon(45px 0,100% 0,100% 100%,0 100%)}
.top-phone{left:682px;top:25px;font:400 21px/28px var(--cond);color:var(--white);display:flex;align-items:center;gap:8px}
.btn-outline-white{border:2px solid var(--white);color:var(--white);font:500 15px/1 var(--cond);display:flex;align-items:center;justify-content:center}
.top-quote{left:940px;top:23px;width:104px;height:34px}

.nav{left:0;top:79px;width:1200px;height:51px;background:var(--ink)}
.nav-links{left:160px;top:0;height:51px;display:flex;list-style:none}
.nav-links li{font:500 13px/51px var(--head);color:var(--white);padding:0 12px;position:relative;white-space:nowrap}
.nav-links li.active{color:var(--green)}
.nav-links li.active::after{content:"";position:absolute;left:6px;right:6px;bottom:0;height:3px;background:var(--green)}
.socials{display:flex;gap:10px}
.nav .socials{left:905px;top:11px}
.soc{width:29px;height:29px;border:2px solid var(--green);border-radius:50%;display:flex;align-items:center;justify-content:center}
.soc svg{display:block}
.soc.fill{background:var(--green)}

/* hero */
.hero{left:0;top:130px;width:1200px;height:476px;background:linear-gradient(160deg,#6d6a63,#4a4843 45%,#3b3a36);}
.hero-title{left:0;top:242px;width:1200px;text-align:center;font:300 40px/52px var(--head);color:var(--white)}
.hero-title b{font-weight:600}
.hero-btns{left:0;top:350px;width:1200px;display:flex;justify-content:center;gap:26px}
.hero-btns .btn-outline-white{width:104px;height:32px;font:400 14px/1 var(--head)}

/* services */
.service{width:320px;text-align:center}
.svc-circle{margin:0 auto;width:178px;height:178px;border-radius:50%;background:var(--green);position:relative;display:flex;align-items:center;justify-content:center}
.svc-circle.alt{background:var(--white);box-shadow:0 4px 16px rgba(0,0,0,.18)}
.svc-badge{position:absolute;left:-2px;bottom:2px;width:56px;height:56px;border-radius:50%;background:var(--white);border:4px solid var(--green);display:flex;align-items:center;justify-content:center}
.svc-title{margin-top:34px;font:600 20px/26px var(--head);color:var(--ink)}
.svc-text{margin:12px auto 0;width:300px;font:400 14px/20px var(--head);color:var(--muted)}
.learn{margin-top:34px;font:500 13px/1 var(--cond);color:#444;display:flex;justify-content:center;align-items:center;gap:6px}
.learn.on{color:var(--green)}
.dot{width:12px;height:12px;border-radius:50%;background:#444;display:inline-block}
.learn.on .dot{background:var(--green)}

/* benefits */
.benefits-photo{left:0;top:920px;width:601px;height:462px;background:linear-gradient(180deg,#8aa6c2 0%,#c7d3df 40%,#6e8a4e 70%,#7a786f 100%)}
.benefits{left:601px;top:920px;width:599px;height:462px;background:var(--green);padding:58px 0 0 64px;color:var(--white)}
.benefits h2{font:400 30px/34px var(--head)}
.benefits h3{font:600 19px/26px var(--head)}
.benefit-list{list-style:none;margin-top:22px}
.benefit-list li{display:flex;gap:18px;align-items:flex-start;margin-bottom:14px;font:400 13px/18px var(--head)}
.benefit-list svg{flex:none}
.benefit-btns{display:flex;gap:16px;margin-top:22px}
.btn-white{background:var(--white);color:var(--green);font:500 13px/1 var(--cond);display:flex;align-items:center;justify-content:center;height:34px;width:103px}
.benefit-btns .btn-outline-white{height:34px;width:105px;font-size:13px}

/* about */
.about{left:156px;top:1460px;width:559px}
.about-brand{font:400 30px/36px var(--head);color:var(--ink);letter-spacing:-.5px}
.about-brand span{color:var(--green)}
.acc{margin-top:34px;border-top:1px solid var(--line)}
.acc-item{border-bottom:1px solid var(--line);padding:24px 0}
.acc-head{display:flex;justify-content:space-between;align-items:center;font:600 18px/22px var(--head);color:var(--ink)}
.acc-body{margin-top:14px;font:400 13px/19px var(--head);color:var(--muted)}
.btn-green{background:var(--green);color:var(--white);font:500 13px/1 var(--cond);display:inline-flex;align-items:center;justify-content:center;width:101px;height:33px;margin-top:16px}

.quote-card{left:764px;top:1430px;width:280px;height:434px;background:var(--white);box-shadow:0 4px 20px rgba(0,0,0,.18)}
.quote-head{background:var(--green);color:var(--white);text-align:center;padding:14px 0 12px}
.quote-head h4{font:400 25px/28px var(--cond)}
.quote-head p{font:400 13px/17px var(--head);margin-top:4px}
.quote-form{padding:22px 24px 0 22px}
.field{height:36px;border:1px solid #d5d5d5;margin-bottom:12px;font:400 12px/34px var(--head);color:#aaa;padding-left:14px}
.field.area{height:112px}
.btn-send{margin-top:12px;width:106px;height:34px;border:2px solid var(--green);color:var(--green);font:500 13px/1 var(--cond);display:flex;align-items:center;justify-content:center;gap:6px}

/* testimonial */
.testi{left:0;top:1976px;width:1200px;height:296px;background:linear-gradient(180deg,#9aa3a8,#4c4a45 55%,#3c3a35)}
.avatar{left:541px;top:1918px;width:116px;height:116px;border-radius:50%;background:#c9ccd0;border:6px solid var(--white);box-shadow:0 2px 10px rgba(0,0,0,.2)}
.testi-quote{left:230px;top:2060px;width:740px;text-align:center;font:italic 400 15px/22px var(--head);color:var(--white)}
.testi-name{left:0;top:2170px;width:1200px;text-align:center;font:400 20px/24px var(--head);color:var(--white)}
.testi-role{left:0;top:2200px;width:1200px;text-align:center;font:400 12px/16px var(--head);color:#ddd}

/* gallery */
.gallery-title{left:0;top:2332px;width:1200px;text-align:center;font:400 30px/36px var(--head);color:var(--ink)}
.g-card{top:2393px;height:235px;background:#e9e9e9;padding:8px;display:flex;gap:8px;box-shadow:0 2px 8px rgba(0,0,0,.1)}
.g-pic{flex:1;position:relative}
.g-tag{position:absolute;left:0;right:0;bottom:0;height:32px;background:rgba(30,30,30,.7);color:var(--white);font:500 13px/32px var(--cond);padding-left:10px}
.view-all{left:548px;top:2665px;width:104px;height:32px;border:2px solid var(--green);color:var(--green);font:500 13px/1 var(--cond);display:flex;align-items:center;justify-content:center}

/* cta */
.cta{left:0;top:2761px;width:1200px;height:263px;background:var(--green);text-align:center;color:var(--white)}
.cta h2{margin-top:58px;font:400 29px/36px var(--head)}
.cta p{margin-top:10px;font:400 30px/36px var(--cond);display:flex;justify-content:center;align-items:center;gap:8px}
.cta .btn-outline-white{margin:22px auto 0;width:136px;height:40px;font-size:18px}

/* footer */
.footer{left:0;top:3024px;width:1200px;height:390px;background:var(--ink);color:#bbb}
.f-col{top:56px}
.f-col h5{font:600 18px/22px var(--head);color:var(--white)}
.f-col p{font:400 12px/18px var(--head)}
.f-divider{top:48px;width:1px;height:260px;background:#444}
.stars{display:flex;gap:4px;margin-top:6px}
.f-phone{font:400 21px/26px var(--cond);color:var(--white);margin-top:14px;display:flex;align-items:center;gap:6px}
.f-input{width:280px;height:34px;border:1px solid #555;margin-top:18px;font:italic 400 12px/32px var(--head);color:#888;padding-left:12px}
.f-send{margin-top:18px;width:106px;height:30px;border:2px solid var(--green);color:var(--green);font:500 13px/1 var(--cond);display:flex;align-items:center;justify-content:center;gap:6px}
.f-links{list-style:none;margin-top:18px}
.f-links li{font:400 13px/23px var(--head)}
.f-links li.on{color:var(--green)}

.bottom{left:0;top:3414px;width:1200px;height:81px;background:var(--white);border-top:1px solid #eee}
.copy{left:156px;top:30px;font:400 12px/18px var(--head);color:#888}
.cards{left:838px;top:24px;display:flex;gap:6px}
.card{width:40px;height:26px;border-radius:3px}
</style>
</head>
<body>

<!-- Header -->
<header class="abs topbar">
  <div class="abs brand">Tidlow Haulage</div>
  <div class="abs topbar-green"></div>
  <div class="abs top-phone">Call Us Today:
    <svg width="16" height="20" viewBox="0 0 16 20"><rect x="2" y="1" width="12" height="18" rx="2" fill="none" stroke="#fff" stroke-width="2"/><circle cx="8" cy="15.5" r="1.3" fill="#fff"/></svg>
    0400 555 018</div>
  <a class="abs btn-outline-white top-quote">Get a Quote</a>
</header>

<nav class="abs nav">
  <ul class="abs nav-links">
    <li class="active">Home</li><li>About</li><li>Services</li><li>Gallery</li><li>Faqs</li><li>Testimonials</li><li>Locations</li><li>Blog</li><li>Contact</li>
  </ul>
  <div class="abs socials">
    <span class="soc"><svg width="13" height="13" viewBox="0 0 14 14"><circle cx="3" cy="7" r="2" fill="var(--green)"/><circle cx="11" cy="3" r="2" fill="var(--green)"/><circle cx="11" cy="11" r="2" fill="var(--green)"/><path d="M3 7 11 3M3 7l8 4" stroke="var(--green)" stroke-width="1.3"/></svg></span>
    <span class="soc"><svg width="13" height="11" viewBox="0 0 14 11"><rect x="0.7" y="0.7" width="12.6" height="9.6" fill="none" stroke="var(--green)" stroke-width="1.4"/><path d="M1 1l6 5 6-5" fill="none" stroke="var(--green)" stroke-width="1.4"/></svg></span>
    <span class="soc"><svg width="11" height="14" viewBox="0 0 11 14"><path d="M5.5 0C2.5 0 0 2.3 0 5.3 0 9 5.5 14 5.5 14S11 9 11 5.3C11 2.3 8.5 0 5.5 0z" fill="var(--green)"/><circle cx="5.5" cy="5.3" r="2" fill="var(--ink)"/></svg></span>
    <span class="soc"><svg width="12" height="12" viewBox="0 0 12 12"><path d="M5 0h2v5h5v2H7v5H5V7H0V5h5z" fill="var(--green)"/></svg></span>
  </div>
</nav>

<!-- Hero -->
<section class="abs hero" role="img" aria-label="Photo of a room piled with construction debris and household rubbish, darkened"></section>
<h1 class="abs hero-title">Sydney's <b>Cheapest</b><br><b>Rubbish Removal</b> Services</h1>
<div class="abs hero-btns"><a class="btn-outline-white">Contact Us</a><a class="btn-outline-white">About Us</a></div>

<!-- Services -->
<div class="abs service" style="left:136px;top:518px">
  <div class="svc-circle">
    <svg width="96" height="84" viewBox="0 0 96 84"><path d="M48 6 6 44h12v34h24V56h12v22h24V44h12z" fill="none" stroke="#fff" stroke-width="6" stroke-linejoin="round"/></svg>
    <div class="svc-badge"><svg width="30" height="18" viewBox="0 0 30 18"><rect x="0" y="2" width="18" height="11" fill="#333"/><path d="M18 5h7l4 5v3H18z" fill="#333"/><circle cx="6" cy="15" r="3" fill="#333"/><circle cx="23" cy="15" r="3" fill="#333"/></svg></div>
  </div>
  <div class="svc-title">Residential/Homes</div>
  <p class="svc-text">It is a long established fact that a reader will be distracted by the readable content of a page when looking ...</p>
  <div class="learn"><span class="dot"></span>Learn More</div>
</div>

<div class="abs service" style="left:439px;top:518px">
  <div class="svc-circle alt">
    <svg width="70" height="80" viewBox="0 0 70 80"><rect x="6" y="4" width="32" height="74" fill="var(--green)"/><rect x="38" y="26" width="26" height="52" fill="var(--green)"/><g fill="#fff"><rect x="13" y="12" width="6" height="6"/><rect x="25" y="12" width="6" height="6"/><rect x="13" y="26" width="6" height="6"/><rect x="25" y="26" width="6" height="6"/><rect x="13" y="40" width="6" height="6"/><rect x="25" y="40" width="6" height="6"/><rect x="45" y="34" width="5" height="6"/><rect x="54" y="34" width="5" height="6"/><rect x="45" y="48" width="5" height="6"/><rect x="54" y="48" width="5" height="6"/></g></svg>
    <div class="svc-badge"><svg width="30" height="18" viewBox="0 0 30 18"><rect x="0" y="2" width="18" height="11" fill="#333"/><path d="M18 5h7l4 5v3H18z" fill="#333"/><circle cx="6" cy="15" r="3" fill="#333"/><circle cx="23" cy="15" r="3" fill="#333"/></svg></div>
  </div>
  <div class="svc-title">Office/Commercial</div>
  <p class="svc-text">It is a long established fact that a reader will be distracted by the readable content of a page when looking ...</p>
  <div class="learn"><span class="dot"></span>Learn More</div>
</div>

<div class="abs service" style="left:744px;top:518px">
  <div class="svc-circle">
    <svg width="84" height="84" viewBox="0 0 84 84"><g fill="none" stroke="#fff" stroke-width="5"><path d="M22 60V12L72 30"/><path d="M22 12 8 24"/><path d="M62 26v20"/></g><rect x="10" y="60" width="46" height="16" rx="6" fill="#fff"/><rect x="56" y="46" width="16" height="10" fill="#fff"/></svg>
    <div class="svc-badge"><svg width="30" height="18" viewBox="0 0 30 18"><rect x="0" y="2" width="18" height="11" fill="#333"/><path d="M18 5h7l4 5v3H18z" fill="#333"/><circle cx="6" cy="15" r="3" fill="#333"/><circle cx="23" cy="15" r="3" fill="#333"/></svg></div>
  </div>
  <div class="svc-title">Construction/Demolition</div>
  <p class="svc-text">It is a long established fact that a reader will be distracted by the readable content of a page when looking ...</p>
  <div class="learn on"><span class="dot"></span>Learn More</div>
</div>

<!-- Benefits -->
<div class="abs benefits-photo" role="img" aria-label="Photo of a green and white rubbish collection truck lifting a bin on a suburban street"></div>
<section class="abs benefits">
  <h2>Benefits to working</h2>
  <h3>with Tidlow Haulage</h3>
  <ul class="benefit-list">
    <li><svg width="34" height="34" viewBox="0 0 34 34"><circle cx="17" cy="17" r="15" fill="none" stroke="#fff" stroke-width="2"/><path d="M10 17l5 5 10-11" fill="none" stroke="#fff" stroke-width="2.5"/></svg>Builders rubbish removal including demolition,<br>strip outs and labour hire</li>
    <li><svg width="34" height="34" viewBox="0 0 34 34"><circle cx="17" cy="17" r="15" fill="none" stroke="#fff" stroke-width="2"/><path d="M10 17l5 5 10-11" fill="none" stroke="#fff" stroke-width="2.5"/></svg>Private rubbish removal including white goods,<br>garden rubbish and furniture</li>
    <li><svg width="34" height="34" viewBox="0 0 34 34"><circle cx="17" cy="17" r="15" fill="none" stroke="#fff" stroke-width="2"/><path d="M10 17l5 5 10-11" fill="none" stroke="#fff" stroke-width="2.5"/></svg>All rubbish removal – no job is too large, too<br>small or too difficult</li>
    <li><svg width="34" height="34" viewBox="0 0 34 34"><circle cx="17" cy="17" r="15" fill="none" stroke="#fff" stroke-width="2"/><path d="M10 17l5 5 10-11" fill="none" stroke="#fff" stroke-width="2.5"/></svg>Better pricing for regular<br>customers</li>
  </ul>
  <div class="benefit-btns"><a class="btn-white">Call Us Today</a><a class="btn-outline-white">Free Quote</a></div>
</section>

<!-- About -->
<section class="abs about">
  <div class="about-brand">Tidlow<span>Haulage</span></div>
  <div class="acc">
    <div class="acc-item">
      <div class="acc-head">About Us <svg width="14" height="14"><circle cx="7" cy="7" r="7" fill="var(--green)"/><rect x="3" y="6" width="8" height="2" fill="#fff"/></svg></div>
      <p class="acc-body">Tidlow Haulage offers complete rubbish removal services for your home or business including residential households, offices, retail locations, building sites, demolition and more. We are a trusted Sydney rubbish removal company that handles the most demanding work – and we ensure that your rubbish is always recycled, ...</p>
      <a class="btn-green">Discover More</a>
    </div>
    <div class="acc-item">
      <div class="acc-head">Why Us <svg width="14" height="14"><circle cx="7" cy="7" r="7" fill="#444"/><rect x="3" y="6" width="8" height="2" fill="#fff"/><rect x="6" y="3" width="2" height="8" fill="#fff"/></svg></div>
    </div>
  </div>
</section>

<aside class="abs quote-card">
  <div class="quote-head"><h4>Get a Quote</h4><p>Enquire now and we call back<br>within 60 minutes!</p></div>
  <div class="quote-form">
    <div class="field">Name</div>
    <div class="field">Email</div>
    <div class="field">Phone</div>
    <div class="field area">Message ...</div>
    <a class="btn-send"><svg width="14" height="12" viewBox="0 0 14 12"><path d="M0 5 14 0 10 12 7 7z" fill="var(--green)"/></svg>Send</a>
  </div>
</aside>

<!-- Testimonial -->
<section class="abs testi" role="img" aria-label="Photo of a skip bin overflowing with household rubbish, darkened"></section>
<div class="abs avatar" role="img" aria-label="Customer portrait"></div>
<svg class="abs" style="left:150px;top:2100px" width="30" height="22" viewBox="0 0 30 22"><path d="M12 0 0 9l12 9v-5c8 0 13 2 18 9-2-9-7-15-18-15z" fill="#fff"/></svg>
<svg class="abs" style="left:1020px;top:2100px" width="30" height="22" viewBox="0 0 30 22"><path d="M18 0l12 9-12 9v-5C10 13 5 15 0 22 2 13 7 7 18 7z" fill="var(--green)"/></svg>
<p class="abs testi-quote">"Excellent service, quote given on the spot for major clean-up of household throw-outs. The team provides quick, efficient and courteous removal! Very satisfied customer."</p>
<div class="abs testi-name">Mark Dalby - Coogee</div>
<div class="abs testi-role">- Residential Rubbish Removal -</div>

<!-- Gallery -->
<h2 class="abs gallery-title">Gallery</h2>
<svg class="abs" style="left:152px;top:2500px" width="26" height="20" viewBox="0 0 30 22"><path d="M12 0 0 9l12 9v-5c8 0 13 2 18 9-2-9-7-15-18-15z" fill="#666"/></svg>
<svg class="abs" style="left:1020px;top:2500px" width="26" height="20" viewBox="0 0 30 22"><path d="M18 0l12 9-12 9v-5C10 13 5 15 0 22 2 13 7 7 18 7z" fill="#666"/></svg>
<div class="abs g-card" style="left:233px;width:342px">
  <div class="g-pic" role="img" aria-label="Narrow side path cluttered with garden rubbish, before" style="background:linear-gradient(180deg,#6d8a4e,#8a7c66)"><span class="g-tag">Before</span></div>
  <div class="g-pic" role="img" aria-label="Same side path cleared, after" style="background:linear-gradient(180deg,#5e8040,#9a9a94)"><span class="g-tag">After</span></div>
</div>
<svg class="abs" style="left:392px;top:2490px" width="34" height="34" viewBox="0 0 34 34"><circle cx="17" cy="17" r="17" fill="var(--green)"/><path d="M10 17l5 5 10-11" fill="none" stroke="#fff" stroke-width="3"/></svg>
<div class="abs g-card" style="left:613px;width:352px">
  <div class="g-pic" role="img" aria-label="Backyard piled with household junk, before" style="background:linear-gradient(180deg,#6f7d5a,#9b6a5a)"><span class="g-tag">Before</span></div>
  <div class="g-pic" role="img" aria-label="Same backyard cleared to grass, after" style="background:linear-gradient(180deg,#8aa35e,#6a9a3c)"><span class="g-tag">After</span></div>
</div>
<a class="abs view-all">View All</a>

<!-- CTA -->
<section class="abs cta">
  <h2>Get a Complimentary Junk Removal Quote Today!</h2>
  <p>Call Us <svg width="18" height="24" viewBox="0 0 16 20"><rect x="2" y="1" width="12" height="18" rx="2" fill="none" stroke="#fff" stroke-width="2"/><circle cx="8" cy="15.5" r="1.3" fill="#fff"/></svg> 0400 555 018 or Email Us</p>
  <a class="btn-outline-white">Get a Quote</a>
</section>

<!-- Footer -->
<footer class="abs footer">
  <div class="abs f-col" style="left:156px;width:300px">
    <h5>Tidlow Haulage</h5>
    <p style="margin-top:18px">Sydney, NSW<br>Monday through to Sunday, all day</p>
    <h5 style="font-size:13px;margin-top:20px">Reviews</h5>
    <div class="stars">
      <svg width="18" height="18" viewBox="0 0 24 24"><path d="M12 1l3.4 7 7.6 1-5.5 5.3 1.3 7.6L12 18.3 5.2 21.9l1.3-7.6L1 9l7.6-1z" fill="var(--green)"/></svg>
      <svg width="18" height="18" viewBox="0 0 24 24"><path d="M12 1l3.4 7 7.6 1-5.5 5.3 1.3 7.6L12 18.3 5.2 21.9l1.3-7.6L1 9l7.6-1z" fill="var(--green)"/></svg>
      <svg width="18" height="18" viewBox="0 0 24 24"><path d="M12 1l3.4 7 7.6 1-5.5 5.3 1.3 7.6L12 18.3 5.2 21.9l1.3-7.6L1 9l7.6-1z" fill="var(--green)"/></svg>
      <svg width="18" height="18" viewBox="0 0 24 24"><path d="M12 1l3.4 7 7.6 1-5.5 5.3 1.3 7.6L12 18.3 5.2 21.9l1.3-7.6L1 9l7.6-1z" fill="var(--green)"/></svg>
      <svg width="18" height="18" viewBox="0 0 24 24"><path d="M12 1l3.4 7 7.6 1-5.5 5.3 1.3 7.6L12 18.3 5.2 21.9l1.3-7.6L1 9l7.6-1z" fill="none" stroke="var(--green)" stroke-width="2"/></svg>
    </div>
    <p style="color:var(--green)">4.9 out of 5</p>
    <div class="f-phone">Call Us <svg width="13" height="17" viewBox="0 0 16 20"><rect x="2" y="1" width="12" height="18" rx="2" fill="none" stroke="#fff" stroke-width="2"/><circle cx="8" cy="15.5" r="1.3" fill="#fff"/></svg> 0400 555 018</div>
    <p>hello@tidlowhaulage.com.au</p>
    <div class="socials" style="margin-top:22px">
      <span class="soc"><svg width="13" height="13" viewBox="0 0 14 14"><circle cx="3" cy="7" r="2" fill="var(--green)"/><circle cx="11" cy="3" r="2" fill="var(--green)"/><circle cx="11" cy="11" r="2" fill="var(--green)"/><path d="M3 7 11 3M3 7l8 4" stroke="var(--green)" stroke-width="1.3"/></svg></span>
      <span class="soc fill"><svg width="13" height="11" viewBox="0 0 14 11"><rect x="0.7" y="0.7" width="12.6" height="9.6" fill="none" stroke="#fff" stroke-width="1.4"/><path d="M1 1l6 5 6-5" fill="none" stroke="#fff" stroke-width="1.4"/></svg></span>
      <span class="soc"><svg width="11" height="14" viewBox="0 0 11 14"><path d="M5.5 0C2.5 0 0 2.3 0 5.3 0 9 5.5 14 5.5 14S11 9 11 5.3C11 2.3 8.5 0 5.5 0z" fill="var(--green)"/><circle cx="5.5" cy="5.3" r="2" fill="var(--ink)"/></svg></span>
      <span class="soc"><svg width="12" height="12" viewBox="0 0 12 12"><path d="M5 0h2v5h5v2H7v5H5V7H0V5h5z" fill="var(--green)"/></svg></span>
    </div>
  </div>
  <div class="abs f-divider" style="left:482px"></div>
  <div class="abs f-col" style="left:536px;width:300px">
    <h5>Newsletter</h5>
    <p style="margin-top:18px">Subscribe to our Newsletter to get the<br>latest scoop right to your inbox.</p>
    <div class="f-input">Enter your email ...</div>
    <a class="f-send"><svg width="14" height="12" viewBox="0 0 14 12"><path d="M0 5 14 0 10 12 7 7z" fill="var(--green)"/></svg>Send</a>
  </div>
  <div class="abs f-divider" style="left:868px"></div>
  <div class="abs f-col" style="left:916px;width:140px">
    <h5>Quick Link</h5>
    <ul class="f-links"><li>About</li><li class="on">Services</li><li>Gallery</li><li>Faqs</li><li>Testimonials</li><li>Locations</li><li>Blog</li><li>Contact</li></ul>
  </div>
</footer>

<div class="abs bottom">
  <p class="abs copy">© 2016 Tidlow Haulage. All rights reserved.</p>
  <div class="abs cards"><span class="card" style="background:#c8ccd6"></span><span class="card" style="background:#d9c3b8"></span><span class="card" style="background:#cfcfcf"></span></div>
  <svg class="abs" style="left:1028px;top:28px" width="18" height="20" viewBox="0 0 18 20"><path d="M9 0 0 9h6v11h6V9h6z" fill="var(--green)"/></svg>
</div>

</body>
</html>
```